Edit of business card / magnet

Hi there
Can you please edit the attached business card which I am going to use to print on a magnet. Can you please edit the following:
1) Make it 54 x 90mm with a 3 mm bleed.
2) I need 3 different versions. Each version will be the same with the exception of the following sentence which I need added underneath the Pinecrest Plumbing Services Pty Limited logo:
i) Your local Cherrybrook plumber
ii) Your local Wahroonga plumber
iii) Your local St Ives plumber
3) Can you add the wording "Present this card to receive a $50 discount" somewhere
4) On the right hand side where it lists the different types of services can you add a point "we can work within your budget"
Thanks

```html
<!DOCTYPE html>
<html lang="en">
<head>
<meta charset="utf-8">
<title>Pinecrest Plumbing – Business Card</title>
<link rel="stylesheet" href="https://fonts.googleapis.com/css2?family=Cabin:wght@400;500;600;700&family=Arimo:wght@400;700&display=swap">
<style>
  :root {
    --brand-blue: #0077c0;
    --text-grey: #6d6e71;
    --white: #ffffff;
    --note-gold: #d9b84a;
  }
  * { margin: 0; padding: 0; box-sizing: border-box; }
  html, body {
    width: 1200px;
    height: 750px;
    overflow: hidden;
    background: var(--white);
  }
  .card {
    position: relative;
    width: 1200px;
    height: 750px;
    background: var(--white);
    font-family: "Cabin", "Gill Sans", sans-serif;
  }

  /* Left: business name + tagline */
  .brand-name {
    position: absolute;
    left: 90px;
    top: 350px;
    width: 460px;
    text-align: center;
    color: var(--brand-blue);
    font-weight: 600;
    line-height: 1;
  }
  .brand-name .name-main {
    display: block;
    font-size: 62px;
    letter-spacing: -1px;
  }
  .brand-name .name-sub {
    display: block;
    margin-top: 10px;
    font-size: 26px;
    letter-spacing: 1px;
    text-transform: uppercase;
  }
  .tagline {
    position: absolute;
    left: 40px;
    top: 600px;
    width: 560px;
    text-align: center;
    font-family: "Arimo", Arial, sans-serif;
    font-size: 22px;
    color: var(--text-grey);
    letter-spacing: 0.5px;
  }
  .tagline .suburb {
    font-weight: 700;
    font-size: 28px;
    color: var(--brand-blue);
    letter-spacing: 1px;
  }

  /* Right: blue services panel */
  .services-panel {
    position: absolute;
    left: 597px;
    top: 37px;
    width: 560px;
    height: 671px;
    background: var(--brand-blue);
    color: var(--white);
  }
  .service-list {
    list-style: none;
    position: absolute;
    right: 45px;
    top: 82px;
    text-align: right;
    font-size: 32px;
    line-height: 50px;
    letter-spacing: -0.3px;
  }
  .budget-note {
    position: absolute;
    right: 45px;
    top: 320px;
    text-align: right;
    font-size: 32px;
    line-height: 37px;
    letter-spacing: -0.3px;
  }
  .contact {
    position: absolute;
    right: 45px;
    top: 440px;
    text-align: right;
  }
  .contact .licence {
    font-size: 19px;
    line-height: 30px;
  }
  .contact .phone {
    font-size: 26px;
    font-weight: 600;
    line-height: 40px;
    letter-spacing: 1px;
  }
  .contact .online {
    font-size: 25px;
    line-height: 37px;
  }
  .discount-offer {
    position: absolute;
    left: 28px;
    top: 616px;
    display: flex;
    align-items: center;
    gap: 14px;
    font-family: "Arimo", Arial, sans-serif;
    font-size: 16px;
    letter-spacing: 0.2px;
  }
  .cash-graphic {
    display: block;
    width: 56px;
    height: 34px;
    border-radius: 3px;
    background: linear-gradient(135deg, var(--note-gold), #c9a23a);
  }
</style>
</head>
<body>
  <div class="card">
    <div class="brand-name">
      <span class="name-main">Pinecrest<br>Plumbing</span>
      <span class="name-sub">Services Pty Ltd</span>
    </div>
    <p class="tagline">Your local <span class="suburb">Cherrybrook</span> plumber</p>

    <section class="services-panel">
      <ul class="service-list">
        <li>PLUMBING SERVICES</li>
        <li>HOT WATER SYSTEMS</li>
        <li>GAS SERVICES</li>
        <li>BLOCKED DRAINS</li>
        <li>TAPS TOILETS</li>
      </ul>
      <p class="budget-note">WE CAN WORK<br>WITHIN YOUR BUDGET</p>
      <div class="contact">
        <p class="licence">Lic #318207c</p>
        <p class="phone">0400 555 218</p>
        <p class="online">enquiry@pinecrestplumbing.com.au</p>
        <p class="online">www.pinecrestplumbing.com.au</p>
      </div>
      <div class="discount-offer">
        <span class="cash-graphic" role="img" aria-label="Illustration of Australian fifty dollar banknotes"></span>
        <span>PRESENT THIS CARD TO RECEIVE A $50 DISCOUNT.</span>
      </div>
    </section>
  </div>
</body>
</html>
```